After tattoo calming solution

The label has to be modern, along the same lines as skin care brand “Plain Form.” It has to reflect the solutions natural effectiveness and simplicity. The label cannot be over fussy, and must be a little bit clinical, as it really does work. The colours should reflect that the solution calms the skin.

We use a 100ml spray bottle.

Target Market(s)

Anyone with a new tattoo or piercing

Industry/Entity Type

Skincare

Requirements
Must have
• Must reflect its natural calming but still remain a little clinical
Should not have
• It must not look like other flowery tattoo cream solutions.

```html
<!DOCTYPE html>
<html lang="en">
<head>
<meta charset="utf-8">
<title>Stillmark – Expert Repair Spray Label Options</title>
<link href="https://fonts.googleapis.com/css2?family=Libre+Baskerville&family=Open+Sans:wght@400&display=swap" rel="stylesheet">
<style>
  :root {
    --backdrop: #c9c9c9;
    --label: #fbfbfb;
    --ink: #3a3a3a;
    --ink-soft: #4a4a4a;
    --caption: #6f6f6f;
    --calm-light: #8fcbe0;
    --calm-deep: #3e9ec0;
    --vivid-light: #5ec3e6;
    --vivid-deep: #1b8ec6;
    --rule: #a9d6e6;
  }
  * { margin: 0; padding: 0; box-sizing: border-box; }
  html, body { width: 1200px; height: 1200px; overflow: hidden; }
  body {
    background: var(--backdrop);
    position: relative;
    font-family: "Open Sans", sans-serif;
  }
  .label {
    position: absolute;
    top: 330px;
    width: 270px;
    height: 730px;
    background: var(--label);
    border-radius: 6px;
  }
  .label--g { left: 248px; }
  .label--h { left: 697px; }
  .label__content {
    position: absolute;
    left: 36px;
    right: 36px;
  }
  .brand-name {
    font-family: "Libre Baskerville", serif;
    font-size: 22px;
    letter-spacing: 1px;
    color: var(--ink);
    white-space: nowrap;
  }
  .headline {
    font-family: "Libre Baskerville", serif;
    font-size: 30px;
    line-height: 35px;
    letter-spacing: -0.3px;
    white-space: nowrap;
    -webkit-background-clip: text;
    background-clip: text;
    color: transparent;
  }
  .label--g .headline {
    background-image: linear-gradient(100deg, var(--calm-light) 0%, var(--calm-deep) 100%);
  }
  .label--h .headline {
    background-image: linear-gradient(100deg, var(--vivid-light) 0%, var(--vivid-deep) 100%);
  }
  .headline-rule {
    height: 1px;
    background: var(--rule);
    margin-top: 6px;
  }
  .benefit {
    font-size: 15px;
    line-height: 21px;
    color: var(--ink-soft);
    white-space: nowrap;
  }
  .volume {
    font-family: "Libre Baskerville", serif;
    font-size: 21px;
    color: var(--ink);
    white-space: nowrap;
  }
  .volume__mark { font-size: 26px; }
  .option-caption {
    position: absolute;
    top: 1122px;
    width: 270px;
    text-align: center;
    font-size: 19px;
    letter-spacing: 4px;
    color: var(--caption);
  }
  .option-caption--g { left: 248px; }
  .option-caption--h { left: 697px; }
</style>
</head>
<body>

<section class="label label--g">
  <div class="label__content" style="top:244px;">
    <p class="brand-name">Stillmark</p>
  </div>
  <div class="label__content" style="top:330px;">
    <h1 class="headline">expert<br>repair for<br>new tattoos<br>&amp; piercings</h1>
    <div class="headline-rule"></div>
  </div>
  <div class="label__content" style="top:488px;">
    <p class="benefit">Reduces inflammation,<br>irritation and encourages<br>natural skin healing</p>
  </div>
  <div class="label__content" style="top:598px;">
    <p class="volume">100 ml <span class="volume__mark">&#8494;</span> 3.4 fl oz</p>
  </div>
</section>

<section class="label label--h">
  <div class="label__content" style="top:230px;">
    <h1 class="headline">expert<br>repair for<br>new tattoos<br>&amp; piercings</h1>
  </div>
  <div class="label__content" style="top:386px;">
    <p class="benefit">Reduces inflammation,<br>irritation and encourages<br>natural skin healing</p>
  </div>
  <div class="label__content" style="top:486px;">
    <p class="brand-name">Stillmark</p>
  </div>
  <div class="label__content" style="top:598px;">
    <p class="volume">100 ml <span class="volume__mark">&#8494;</span> 3.4 fl oz</p>
  </div>
</section>

<p class="option-caption option-caption--g">Option G</p>
<p class="option-caption option-caption--h">Option H</p>

</body>
</html>
```